Business Card for a recruitment agency specializing in engineers and geeks.

I am looking to create Business Card Design for my company.
That
## Company name:
Quorvant Inc.
Quorvant is a term coined from the following concepts.
1. geek + engineer
2. geek utopia
## Company Description:
The concept of the company is to be a recruitment agency that creates a paradise for geeky engineers. We want to be a place where engineers can have more freedom and ideal career support.
# Target.
The noun itself is often given to companies that want to hire engineers, geeks, and IT-related personnel, so it would be nice to get the impression that this company seems to have good engineers and IT personnel. There are many occasions where I meet with the human resources department, president, or senior management and give it to them.
# Atmosphere
We are happy with simplicity, but with an impact that will help people remember the company. The logo is based on a dinosaur that does programming, so it should be somewhat playful, but since it will basically be used in a business setting, please don't make it too silly.
# About the logo
See the attached files. The company logo represents our engineers smiling upward because of our work, with the motif of a dinosaur doing programming.
## Color
We will leave the color scheme to you, but since the logo is in black and white, colors with such a taste would fit well.
## file format
ai, psd, png, svg
Industry/Entity Type
human resource and employment agency
Contact Information for Business Card
Company name, address, email, tel, URL,logo
Colors
Designer to choose colors to be used in the design.

```html
<!DOCTYPE html>
<html lang="en">
<head>
<meta charset="utf-8">
<title>Quorvant Inc. — Business Card</title>
<link rel="stylesheet" href="https://fonts.googleapis.com/css2?family=Montserrat:wght@400;600&display=swap">
<style>
  :root {
    --backdrop: #3b3b3b;
    --card: #1a1a1a;
    --card-back: #111111;
    --silver: #d6d6d6;
    --silver-soft: #a9a9a9;
    --rule: #8a8a8a;
  }
  * { box-sizing: border-box; margin: 0; padding: 0; }
  html, body {
    width: 1200px;
    height: 801px;
    overflow: hidden;
    background: var(--backdrop);
    font-family: "Montserrat", sans-serif;
  }
  .stage {
    position: relative;
    width: 1200px;
    height: 801px;
  }
  .card {
    position: absolute;
    top: 246px;
    width: 540px;
    height: 309px;
    border-radius: 3px;
    box-shadow: 0 10px 30px rgba(0,0,0,0.45);
    overflow: hidden;
  }
  .card--front { left: 40px; background: var(--card); }
  .card--back { left: 620px; background: var(--card-back); }

  /* Front */
  .brand {
    position: absolute;
    top: 78px;
    left: 0;
    width: 100%;
    display: flex;
    justify-content: center;
    align-items: center;
    gap: 16px;
  }
  .brand__square {
    width: 34px;
    height: 34px;
    border: 3px solid var(--silver);
    border-radius: 3px;
  }
  .brand__name {
    font-weight: 400;
    font-size: 40px;
    letter-spacing: 0.5px;
    color: var(--silver);
  }
  .details {
    position: absolute;
    top: 168px;
    left: 0;
    width: 100%;
    display: flex;
    justify-content: center;
    align-items: stretch;
  }
  .address {
    text-align: right;
    padding-right: 22px;
    color: var(--silver-soft);
    font-size: 13.5px;
    line-height: 21px;
  }
  .address__company { color: var(--silver); font-weight: 600; }
  .divider { width: 1px; background: var(--rule); }
  .contacts {
    list-style: none;
    padding-left: 22px;
    color: var(--silver-soft);
    font-size: 13.5px;
    line-height: 21px;
  }
  .contacts li { display: flex; align-items: center; gap: 9px; }
  .contacts svg { width: 11px; height: 11px; fill: var(--silver); flex: none; }

  /* Back */
  .back-pattern {
    position: absolute;
    inset: 0;
    background: linear-gradient(125deg, #0c0c0c 0%, #1d1d1d 45%, #2b2b2b 70%, #141414 100%);
  }
  .back-brand {
    position: absolute;
    inset: 0;
    display: flex;
    justify-content: center;
    align-items: center;
    gap: 10px;
  }
  .back-brand__square {
    width: 20px;
    height: 20px;
    border: 2px solid var(--silver);
    border-radius: 2px;
  }
  .back-brand__name {
    font-size: 22px;
    font-weight: 400;
    color: var(--silver);
  }
</style>
</head>
<body>
<main class="stage">
  <section class="card card--front">
    <div class="brand">
      <span class="brand__square"></span>
      <span class="brand__name">Quorvant</span>
    </div>
    <div class="details">
      <address class="address" style="font-style:normal">
        <div class="address__company">Quorvant Inc.</div>
        <div>1180 Harbor Crest Way</div>
        <div>Marlow Bay CA 92601</div>
      </address>
      <span class="divider"></span>
      <ul class="contacts">
        <li>
          <svg viewBox="0 0 12 12" aria-hidden="true"><path d="M2.5 0.8 4.3 3c.3.4.2.9-.1 1.2l-.8.7c.6 1.3 1.5 2.2 2.8 2.8l.7-.8c.3-.3.8-.4 1.2-.1l2.2 1.8c.4.3.4.9.1 1.2l-1 1.1C8.6 11.7 6 10.8 3.6 8.4S.3 3.4 1.1 2.2l1.1-1c.1-.2.2-.4.3-.4Z"/></svg>
          555-013-2847
        </li>
        <li>
          <svg viewBox="0 0 12 12" aria-hidden="true"><path d="M0 2.5h12v7H0z M0.8 3.2 6 6.8l5.2-3.6" fill="none" stroke="#d6d6d6" stroke-width="1.2"/></svg>
          hello@quorvant.com
        </li>
        <li>
          <svg viewBox="0 0 12 12" aria-hidden="true"><circle cx="6" cy="6" r="5.3" fill="none" stroke="#d6d6d6" stroke-width="1.1"/><path d="M0.8 6h10.4M6 0.7c-2.6 2.8-2.6 7.8 0 10.6M6 0.7c2.6 2.8 2.6 7.8 0 10.6" fill="none" stroke="#d6d6d6" stroke-width="0.9"/></svg>
          www.quorvant.com
        </li>
      </ul>
    </div>
  </section>

  <section class="card card--back">
    <div class="back-pattern" role="img" aria-label="Glossy black-on-black repeating pattern of the brand mark covering the card back"></div>
    <div class="back-brand">
      <span class="back-brand__square"></span>
      <span class="back-brand__name">Quorvant</span>
    </div>
  </section>
</main>
</body>
</html>
```